2 page PSD web design

I need a fairly simple website design built in PSD format for a site / blog in the finance niche. My current web address is www.spreadledgerhub.com. Yield Ledger Hub is a site that teaches people how to trade options with a focus on income strategies.

I need a simple homepage built and then another similar template for all other pages including blog posts.

The rough design layout is shown attached excel file. It is similar to www.marcusfelbring.com although I don't like the colors on his site at all. My logo is attached also, so the colours should be aligned with my logo.

In the header section, I will be giving away a free ebook called "Fluff-Free Manual for Calendar Wings" so I will need a 2D and 3D book cover designed as well. The design should be aligned with my logo and site design.

Industry/Entity Type

Finance

Requirements
Must have
• Everything is detailed in the excel file, but here is a list of must have items:

My current logo
ebook design and sign up section
under the ebook sign up section, need a big bold heading - "HELPING YOU TRADE IRON CONDORS AND OTHER INCOME STRATEGIES WITHOUT THE BS"
6 sidebar sections as detailed in excel file
Social Proof at top right, on the same line / level as the logo
"home advertise contact" in the top left in small discreet font
Should not have
• Do not want any photos or images on either of the pages

```html
<!DOCTYPE html>
<html lang="en">
<head>
<meta charset="utf-8">
<title>Yield Ledger Hub</title>
<link href="https://fonts.googleapis.com/css2?family=Ubuntu:wght@400;500;700&display=swap" rel="stylesheet">
<style>
  :root {
    --brand-blue: #1e88d0;
    --link-blue: #1a7bc0;
    --deep-blue: #1a6fa8;
    --dark: #2a2a2a;
    --dark-soft: #3a3a3a;
    --white: #ffffff;
    --pale-blue: #bfe4fb;
    --band-top: #6cc8f5;
    --band-bottom: #1a8bd6;
    --banner-light: #1596dc;
    --banner-dark: #0b5fa6;
    --book-light: #a6d84a;
    --book-dark: #5f9a1e;
    --highlight: #b6f06a;
    --grey-text: #3d3d3d;
  }
  * { box-sizing: border-box; margin: 0; padding: 0; }
  html, body { width: 1200px; height: 420px; overflow: hidden; }
  body {
    position: relative;
    font-family: "Ubuntu", sans-serif;
    background: linear-gradient(#eaf5fd 0, #ffffff 88px, #ffffff 100%);
  }
  .utility-tab {
    position: absolute; left: 784px; top: 0; width: 220px; height: 19px;
    background: var(--dark-soft); border-radius: 0 0 14px 14px;
    display: flex; justify-content: center; align-items: center; gap: 10px;
    color: var(--white); font-size: 11px;
  }
  .utility-tab span.sep { opacity: .8; }
  .logo { position: absolute; left: 204px; top: 26px; display: flex; align-items: center; gap: 12px; }
  .logo-mark { width: 52px; height: 52px; border-radius: 50%; background: var(--brand-blue); }
  .logo-name { font-size: 28px; font-weight: 500; color: var(--brand-blue); letter-spacing: -.3px; }
  .social-proof {
    position: absolute; right: 196px; top: 27px;
    font-size: 13.5px; color: var(--link-blue);
  }
  .social-links { position: absolute; left: 891px; top: 54px; display: flex; gap: 7px; }
  .social-links span { width: 22px; height: 22px; background: var(--dark); border-radius: 3px; }
  .main-nav {
    position: absolute; left: 0; top: 88px; width: 1200px; height: 29px;
    background: linear-gradient(var(--band-top), var(--band-bottom));
  }
  .nav-home {
    position: absolute; left: 193px; top: 0; width: 30px; height: 29px;
    background: var(--dark-soft); display: flex; align-items: center; justify-content: center;
  }
  .nav-item {
    position: absolute; top: 5px; height: 19px; border-radius: 5px;
    background: var(--dark-soft); color: var(--white);
    font-size: 12.5px; display: flex; align-items: center; justify-content: center;
  }
  .signup-banner {
    position: absolute; left: 193px; top: 123px; width: 814px; height: 219px;
    background: radial-gradient(ellipse at 55% 40%, var(--banner-light), var(--banner-dark) 90%);
    color: var(--white);
  }
  .banner-kicker { position: absolute; left: 17px; top: 19px; font-size: 14px; }
  .banner-title { position: absolute; left: 15px; top: 54px; font-size: 23px; line-height: 33px; }
  .banner-title em { font-style: normal; color: var(--highlight); }
  .banner-lede { position: absolute; left: 16px; top: 163px; font-size: 14px; line-height: 20px; }
  .ebook-cover {
    position: absolute; left: 372px; top: 22px; width: 180px; height: 170px;
    background: linear-gradient(135deg, var(--book-light), var(--book-dark));
    border-radius: 6px; transform: rotate(-28deg) skewX(8deg);
    box-shadow: -10px 10px 0 var(--dark);
  }
  .signup-form { position: absolute; left: 583px; top: 0; width: 208px; }
  .form-intro { margin-top: 10px; text-align: center; font-size: 12.5px; line-height: 17px; color: var(--pale-blue); font-weight: 500; }
  .field {
    margin-top: 10px; height: 37px; border-radius: 6px;
    background: linear-gradient(#ffffff, #e2e2e2);
    font-size: 13.5px; color: #8a8a8a; padding: 11px 9px;
  }
  .field + .field { margin-top: 11px; }
  .submit {
    margin-top: 12px; height: 38px; border-radius: 6px;
    background: var(--dark); border: 2px solid #59a8e0;
    font-size: 19px; font-weight: 500; display: flex; align-items: center; justify-content: center;
  }
  .privacy { margin-top: 5px; text-align: center; font-size: 9.5px; line-height: 14px; color: var(--pale-blue); }
  .tagline-band {
    position: absolute; left: 0; top: 350px; width: 1200px; height: 68px;
    background: linear-gradient(#fbfbfb, #e9e9e9);
    border-top: 1px solid #dcdcdc; border-bottom: 1px solid #d4d4d4;
    text-align: center; font-weight: 500; font-size: 19px; letter-spacing: .3px;
  }
  .tagline-band .lead { margin-top: 7px; color: var(--grey-text); }
  .tagline-band .headline { margin-top: 9px; color: var(--deep-blue); }
</style>
</head>
<body>
  <nav class="utility-tab">
    <span>Home</span><span class="sep">|</span><span>Advertise</span><span class="sep">|</span><span>Contact</span>
  </nav>

  <div class="logo">
    <span class="logo-mark"></span>
    <span class="logo-name">Yield Ledger Hub</span>
  </div>

  <p class="social-proof">Join a Community of 4279 Awesome Readers</p>
  <div class="social-links"><span></span><span></span><span></span><span></span></div>

  <nav class="main-nav">
    <span class="nav-home">
      <svg width="18" height="16" viewBox="0 0 18 16"><path d="M9 1 1 8h2.5v7h4v-4h3v4h4V8H17z" fill="#ffffff"/></svg>
    </span>
    <span class="nav-item" style="left:229px;width:134px">Articles and Videos</span>
    <span class="nav-item" style="left:369px;width:133px">Trading Philosophy</span>
    <span class="nav-item" style="left:508px;width:120px">Learning Centre</span>
    <span class="nav-item" style="left:634px;width:83px">Free Tools</span>
    <span class="nav-item" style="left:723px;width:106px">Members Only</span>
    <span class="nav-item" style="left:834px;width:103px">Work With Us</span>
    <span class="nav-item" style="left:942px;width:63px">About</span>
  </nav>

  <section class="signup-banner">
    <p class="banner-kicker">Do You Want To Know The Truth About Iron Condors?</p>
    <h1 class="banner-title" style="font-weight:400">Learn How To Trade This<br>Amazing Option Income<br>Strategy With <em>Free</em> Ebook</h1>
    <p class="banner-lede">I will share with you my blueprint and all my tips and tricks<br>for generating consistent monthly income with iron condors</p>
    <div class="ebook-cover" role="img" aria-label="3D ebook cover for the free option income strategy guide"></div>
    <form class="signup-form">
      <p class="form-intro">Enter Your Details now<br>for Instant Access..</p>
      <div class="field">Name :</div>
      <div class="field">Email Address :</div>
      <div class="submit">Instant Access !</div>
      <p class="privacy">Your information is NEVER<br>shared or sold for any Reason.</p>
    </form>
  </section>

  <section class="tagline-band">
    <p class="lead">BIG BOLD HEADING –</p>
    <h2 class="headline" style="font-size:19px;font-weight:500">HELPING YOU TRADE IRON CONDORS AND OTHER INCOME STRATEGIES WITHOUT THE BS.</h2>
  </section>
</body>
</html>
```